Save the Date card

This will be a Save the Date 5x7 card...preferably Hunter Green background

Annual Fund Leadership Dinner
June 20, 2023. 6:30 pm
Location: The Pellimore's Home
4187 Brindlecove Ridge Rd
Harrison, TN 37598

Other side of card:
We would prayerfully ask that you consider partnering with us as we kick off our Annual Fund this Fall to celebrate our 25 year anniversary as an Academy.
Please direct any questions to Marla Quenby, our Director of Advancement 423-555-0184 x 3617 or advancement@corvellanprep.org

```html
<!DOCTYPE html>
<html lang="en">
<head>
<meta charset="UTF-8">
<title>Annual Fund Leadership Dinner – Save the Date</title>
<link href="https://fonts.googleapis.com/css2?family=League+Spartan:wght@700;800&family=Montserrat:wght@400;500;600;700&display=swap" rel="stylesheet">
<style>
  :root {
    --hunter: #1f3a24;
    --hunter-deep: #1a3320;
    --gold: #a89a5b;
    --gold-light: #c9b865;
    --ink: #1e2e22;
    --white: #ffffff;
    --page: #ececec;
  }
  * { margin: 0; padding: 0; box-sizing: border-box; }
  html, body { width: 1085px; height: 1200px; overflow: hidden; }
  body {
    background: var(--page);
    font-family: "Montserrat", sans-serif;
    position: relative;
  }
  .card {
    position: absolute;
    left: 171px;
    width: 744px;
    height: 531px;
    overflow: hidden;
    background: var(--white);
  }
  .card--front { top: 46px; }
  .card--back { top: 623px; }
  .card__art { position: absolute; inset: 0; width: 744px; height: 531px; }

  .brand {
    position: absolute;
    font-family: "Montserrat", sans-serif;
    font-weight: 700;
    font-size: 17px;
    line-height: 1.15;
    text-align: center;
    letter-spacing: 0.02em;
  }
  .brand--front { left: 612px; top: 58px; width: 106px; color: var(--white); }
  .brand--back { left: 566px; top: 62px; width: 108px; color: var(--hunter); }

  .event-title {
    position: absolute;
    right: 21px;
    top: 203px;
    text-align: right;
    white-space: nowrap;
    font-family: "League Spartan", sans-serif;
    font-weight: 800;
    font-size: 40px;
    line-height: 48px;
    letter-spacing: -0.045em;
  }
  .event-title__line--gold { color: var(--gold); display: block; }
  .event-title__line--green { color: var(--hunter); display: block; }

  .date-pill {
    position: absolute;
    left: 401px;
    top: 331px;
    width: 343px;
    height: 51px;
    background: var(--hunter);
    border-radius: 12px 0 0 12px;
    display: flex;
    align-items: center;
    padding-left: 13px;
    color: var(--white);
    font-weight: 600;
    font-size: 22px;
  }
  .date-pill__time { color: var(--gold); margin-left: 7px; font-weight: 700; }
  .date-pill__icon { position: absolute; right: 20px; top: 8px; }

  .venue {
    position: absolute;
    right: 62px;
    top: 409px;
    text-align: right;
    color: var(--ink);
    font-style: normal;
    font-weight: 500;
    font-size: 17px;
    line-height: 25px;
  }
  .venue__name { color: var(--gold); font-weight: 700; font-size: 19px; }
  .venue__pin { position: absolute; left: 698px; top: 414px; }

  .appeal {
    position: absolute;
    left: 30px;
    top: 36px;
    color: var(--white);
    font-weight: 500;
    font-size: 16.5px;
    line-height: 25px;
  }
  .milestone__num {
    position: absolute;
    left: 40px;
    top: 112px;
    font-family: "League Spartan", sans-serif;
    font-weight: 800;
    font-size: 100px;
    line-height: 100px;
    letter-spacing: -0.12em;
  }
  .milestone__two { color: var(--gold); }
  .milestone__five { color: var(--white); }
  .milestone__year {
    position: absolute; left: 51px; top: 203px;
    color: var(--gold); font-weight: 700; font-size: 26px;
  }
  .milestone__label {
    position: absolute; left: 159px; top: 138px;
    color: var(--gold); font-weight: 700; font-size: 29px;
  }
  .milestone__sub {
    position: absolute; left: 157px; top: 180px;
    color: var(--white); font-weight: 500; font-size: 22px;
  }

  .contact-banner__text {
    position: absolute;
    left: 42px;
    top: 274px;
    color: var(--white);
    font-weight: 500;
    font-size: 16.5px;
    line-height: 26.5px;
  }
  .contact-banner__name {
    color: var(--hunter);
    font-weight: 700;
    font-size: 19.5px;
    letter-spacing: 0.01em;
  }

  .contact-line {
    position: absolute;
    left: 26px;
    display: flex;
    align-items: center;
    gap: 10px;
    color: var(--white);
  }
  .contact-line--phone { top: 367px; font-weight: 700; font-size: 19.5px; }
  .contact-line--email { top: 404px; font-weight: 500; font-size: 17.5px; }
  .contact-line__domain { color: var(--gold); }

  .divider {
    position: absolute; left: 24px; top: 449px;
    width: 303px; height: 1px; background: rgba(201,184,101,0.6);
  }
  .social__label {
    position: absolute; left: 26px; top: 462px;
    color: var(--white); font-weight: 500; font-size: 9.5px; letter-spacing: 0.02em;
  }
  .social__list { position: absolute; left: 26px; top: 481px; display: flex; gap: 12px; }
  .social__dot {
    width: 25px; height: 25px; border-radius: 50%;
    background: var(--gold);
  }
</style>
</head>
<body>

<section class="card card--front">
  <svg class="card__art" viewBox="0 0 1240 885" preserveAspectRatio="none" aria-hidden="true">
    <defs>
      <linearGradient id="photoTone" x1="0" y1="0" x2="0" y2="1">
        <stop offset="0" stop-color="#5f7d3e"/>
        <stop offset="0.5" stop-color="#8a7a5e"/>
        <stop offset="1" stop-color="#6b4a36"/>
      </linearGradient>
    </defs>
    <polygon points="0,0 625,0 822,111 0,111" fill="var(--gold)"/>
    <polygon points="625,0 1240,0 1240,341" fill="var(--hunter)"/>
    <polygon points="0,540 495,705 762,885 0,885" fill="var(--hunter)"/>
    <polygon points="0,758 185,885 0,885" fill="var(--gold)"/>
    <path d="M-10,108 Q292,-48 600,108 L600,520 Q572,692 292,832 Q12,692 -10,520 Z" fill="var(--white)"/>
    <path d="M2,122 Q292,-28 588,120 L588,515 Q560,682 292,815 Q24,682 2,515 Z" fill="var(--gold)"/>
    <path d="M14,136 Q292,-2 575,133 L575,510 Q548,670 292,795 Q36,670 14,510 Z" fill="var(--hunter)"/>
    <path d="M34,152 Q292,32 555,150 L555,500 Q530,650 292,768 Q54,650 34,500 Z" fill="url(#photoTone)"/>
    <rect x="34" y="80" width="521" height="690" fill="none" role="img" aria-label="Photo of guests toasting with wine around a dinner table"/>
  </svg>

  <div class="brand brand--front">Corvellan<br>Prep</div>

  <h1 class="event-title">
    <span class="event-title__line--gold">ANNUAL FUND</span>
    <span class="event-title__line--green">LEADERSHIP DINNER</span>
  </h1>

  <div class="date-pill">
    <span>June 20, 2023</span><span class="date-pill__time">6:30 pm</span>
    <svg class="date-pill__icon" width="32" height="32" viewBox="0 0 32 32" aria-hidden="true">
      <rect x="2" y="5" width="25" height="24" rx="3" fill="none" stroke="#fff" stroke-width="2"/>
      <line x1="2" y1="11" x2="27" y2="11" stroke="#fff" stroke-width="2"/>
      <line x1="8" y1="2" x2="8" y2="7" stroke="#fff" stroke-width="2"/>
      <line x1="14" y1="2" x2="14" y2="7" stroke="#fff" stroke-width="2"/>
      <line x1="20" y1="2" x2="20" y2="7" stroke="#fff" stroke-width="2"/>
      <g fill="#fff"><circle cx="7" cy="16" r="1.3"/><circle cx="12" cy="16" r="1.3"/><circle cx="17" cy="16" r="1.3"/><circle cx="7" cy="21" r="1.3"/><circle cx="12" cy="21" r="1.3"/><circle cx="7" cy="25" r="1.3"/></g>
      <circle cx="24" cy="24" r="6" fill="var(--hunter)" stroke="#fff" stroke-width="2"/>
      <polyline points="24,21 24,24 26,25.5" fill="none" stroke="#fff" stroke-width="1.6"/>
    </svg>
  </div>

  <address class="venue">
    <div class="venue__name">The Pellimore's Home</div>
    <div>4187 Brindlecove Ridge Rd</div>
    <div>Harrison, TN 37598</div>
  </address>
  <svg class="venue__pin" width="26" height="33" viewBox="0 0 26 33" aria-hidden="true">
    <path d="M13,1 C6,1 1,6 1,12.5 C1,21 13,32 13,32 C13,32 25,21 25,12.5 C25,6 20,1 13,1 Z" fill="var(--hunter)"/>
    <circle cx="13" cy="12.5" r="4.5" fill="#fff"/>
  </svg>
</section>

<section class="card card--back">
  <svg class="card__art" viewBox="0 0 1240 885" preserveAspectRatio="none" aria-hidden="true">
    <defs>
      <linearGradient id="bannerGold" x1="0" y1="0" x2="1" y2="0">
        <stop offset="0" stop-color="#9d8f55"/>
        <stop offset="1" stop-color="#cdb968"/>
      </linearGradient>
      <linearGradient id="stripeGold" x1="0" y1="0" x2="0" y2="1">
        <stop offset="0" stop-color="#a89a5b"/>
        <stop offset="1" stop-color="#d2c06a"/>
      </linearGradient>
      <linearGradient id="stripeMist" x1="0" y1="0" x2="0" y2="1">
        <stop offset="0" stop-color="#e3e5e3"/>
        <stop offset="1" stop-color="#ffffff"/>
      </linearGradient>
      <linearGradient id="panelGreen" x1="0" y1="0" x2="0" y2="1">
        <stop offset="0" stop-color="var(--hunter-deep)"/>
        <stop offset="1" stop-color="#264a30"/>
      </linearGradient>
    </defs>
    <polygon points="0,0 830,0 600,885 0,885" fill="url(#panelGreen)"/>
    <polygon points="836,0 871,0 806,249 780,249" fill="url(#stripeGold)"/>
    <polygon points="785,287 800,287 720,582 700,582" fill="url(#stripeMist)"/>
    <polygon points="685,624 708,624 641,885 613,885" fill="#2b5532"/>
    <polygon points="0,428 668,428 620,605 0,605" fill="url(#bannerGold)"/>
    <polyline points="45,500 45,441 108,441" fill="none" stroke="#fff" stroke-width="1.5"/>
    <polyline points="498,592 562,592 562,530" fill="none" stroke="#fff" stroke-width="1.5"/>
  </svg>

  <div class="brand brand--back">Corvellan<br>Prep</div>

  <p class="appeal">We would prayerfully ask that you<br>consider partnering with us as we kick off our<br>Annual Fund this Fall to celebrate our</p>

  <div class="milestone__num"><span class="milestone__two">2</span><span class="milestone__five">5</span></div>
  <div class="milestone__year">Year</div>
  <div class="milestone__label">Anniversary</div>
  <div class="milestone__sub">as an Academy.</div>

  <p class="contact-banner__text">Please direct any questions to<br><span class="contact-banner__name">MARLA QUENBY</span><br>our Director of Advancement</p>

  <div class="contact-line contact-line--phone">
    <svg width="14" height="16" viewBox="0 0 14 16" aria-hidden="true">
      <path d="M3,1 L5.5,1 L6.5,5 L4.8,6.3 C5.6,8.4 6.8,9.8 8.6,10.8 L10,9.2 L13,10.5 L12.6,13.5 C7,14 1.5,8 2,2 Z" fill="none" stroke="var(--gold)" stroke-width="1.5"/>
    </svg>
    <span>423-555-0184 / 423-555- 3617</span>
  </div>
  <div class="contact-line contact-line--email">
    <svg width="15" height="11" viewBox="0 0 15 11" aria-hidden="true">
      <rect x="0.5" y="0.5" width="14" height="10" fill="var(--gold)"/>
      <polyline points="0.5,0.5 7.5,6 14.5,0.5" fill="none" stroke="var(--hunter)" stroke-width="1.2"/>
    </svg>
    <span>advancement@<span class="contact-line__domain">corvellanprep</span>.org</span>
  </div>

  <div class="divider"></div>
  <div class="social__label">FOLLOW US ON SOCIAL-</div>
  <div class="social__list">
    <span class="social__dot"></span>
    <span class="social__dot"></span>
    <span class="social__dot"></span>
    <span class="social__dot"></span>
    <span class="social__dot"></span>
  </div>
</section>

</body>
</html>
```